New Dental Office Needs an Attractive and user friendly Website Designed

I need a website for a new dental office. The Name is Maplecrest Dentistry. I would like a Modern design with a user friendly interface and usability.
I would like a landing page, a page that lists the services we offer: Cosmetic Dentistry, Implants, Dental Hygiene, Emergency Services, Restorations, Dentures
Target Market(s)
Mid to upper class
Industry/Entity Type
Dentistry
Coding
Coded - Design and coding required
Number of Pages Required
1 page
Requirements
Must have
- Landing page that has a scheduling option, Procedures, operating hours, and contact us info
Nice to have
- Appealing design, Soft comforting colors. Easy to navigate page, Modern and professional.

```html
<!DOCTYPE html>
<html lang="en">
<head>
<meta charset="utf-8">
<title>Maplecrest Dentistry</title>
<link href="https://fonts.googleapis.com/css2?family=Outfit:wght@400;500;600;700;800&display=swap" rel="stylesheet">
<style>
:root{
  --blue:#1a7fd4;
  --blue-light:#3aa5f0;
  --navy:#0b2c57;
  --navy-deep:#0a2446;
  --ink:#2b2b2b;
  --text:#3a3a3a;
  --muted:#8a8f98;
  --line:#dcdfe4;
  --white:#ffffff;
}
*{box-sizing:border-box;margin:0;padding:0}
html,body{width:1200px;height:3866px;overflow:hidden}
body{position:relative;font-family:"Outfit",sans-serif;color:var(--text);background:var(--white)}
.abs{position:absolute}
a{color:inherit;text-decoration:none}
.btn-dark{position:absolute;display:flex;align-items:center;justify-content:center;background:var(--ink);color:var(--white);font-weight:600;font-size:13px;border-radius:5px}
.btn-light{position:absolute;display:flex;align-items:center;justify-content:center;background:var(--white);color:var(--ink);font-weight:600;font-size:13px;border-radius:5px}

/* header */
.site-header{top:0;left:0;width:1200px;height:63px;background:var(--white)}
.brand{display:flex;align-items:center;gap:8px}
.brand-mark{width:26px;height:26px;border-radius:50%;background:var(--blue)}
.brand-name{font-weight:700;font-size:15px;line-height:15px;color:var(--ink)}
.main-nav{left:420px;top:23px;display:flex;gap:25px;font-size:12.5px;font-weight:500;color:var(--ink)}
.main-nav .active{color:var(--blue);text-decoration:underline}
.help{left:774px;top:16px;display:flex;gap:9px;align-items:center}
.icon-sq{width:28px;height:28px;border-radius:6px;background:var(--blue);display:flex;align-items:center;justify-content:center}
.help small{display:block;font-size:9px;color:var(--muted)}
.help strong{font-size:12px;color:var(--ink)}

/* hero */
.hero{top:63px;left:0;width:1200px;height:530px;background:linear-gradient(90deg,#f4f6f8 0%,#e9eef2 45%,#cfdce6 70%,#b9cad7 100%)}
.hero-title{left:156px;top:135px;font-size:49px;font-weight:800;line-height:52px;color:var(--blue);letter-spacing:-1px}
.hero-text{left:156px;top:248px;width:330px;font-size:13.5px;line-height:19px;color:var(--ink)}
.hero-photo{left:640px;top:0;width:560px;height:470px;background:radial-gradient(ellipse at 55% 35%,#e8c9b4 0%,#d7b49b 22%,#c7d3dc 50%,rgba(185,202,215,0) 75%)}

/* about */
.about-shadow{left:170px;top:688px;width:374px;height:358px;border-radius:12px;background:#23262b}
.about-photo{left:156px;top:672px;width:382px;height:374px;border-radius:12px;background:linear-gradient(135deg,#d9c0b0 0%,#c8a591 35%,#9fb9cf 60%,#6fa8de 100%)}
.badge{left:388px;top:906px;width:196px;height:77px;border-radius:4px;background:var(--blue);border:3px solid var(--white);display:flex;align-items:center;gap:10px;padding-left:24px;color:var(--white)}
.badge b{font-size:40px;font-weight:700}
.badge span{font-size:15px;font-weight:600;line-height:16px}
.section-title{font-size:34px;font-weight:800;color:var(--blue);letter-spacing:-.5px}
.about-title{left:642px;top:704px}
.about-copy{left:642px;top:756px;width:390px;font-size:11.5px;line-height:17.5px;color:var(--text)}
.about-copy p+p{margin-top:15px}
.about-contact{top:915px;display:flex;gap:10px;align-items:center}
.dot-icon{width:32px;height:32px;border-radius:50%;background:#cfe4f8;display:flex;align-items:center;justify-content:center}
.about-contact small{display:block;font-size:8.5px;color:var(--muted)}
.about-contact strong{font-size:12px;color:var(--ink)}

/* services */
.services{top:1120px;left:0;width:1200px;height:860px;background:var(--navy)}
.services-title{top:70px;width:1200px;text-align:center;font-size:32px;font-weight:800;color:var(--white)}
.service-card{width:279px;height:250px;background:var(--white);border-radius:10px;padding:3px}
.service-head{height:68px;position:relative}
.service-icon{position:absolute;left:18px;top:8px;width:66px;height:66px;border-radius:50%;background:var(--white);box-shadow:0 2px 8px rgba(0,0,0,.12);display:flex;align-items:center;justify-content:center;z-index:2}
.service-name{position:absolute;left:106px;top:18px;font-size:16px;font-weight:700;line-height:17px;color:var(--ink)}
.service-name.single{top:27px}
.service-photo{height:176px;border-radius:0 0 8px 8px}

/* team */
.team-title{left:156px;top:2083px}
.team-lead{left:156px;top:2132px;width:240px;font-size:10px;font-weight:700;line-height:14px;color:var(--ink)}
.team-copy{left:156px;top:2168px;width:240px;font-size:9.5px;line-height:14px;color:var(--text)}
.team-card{top:2050px;width:182px;height:263px;background:var(--white);box-shadow:0 2px 10px rgba(0,0,0,.09);padding:6px}
.team-photo{height:167px}
.team-role{margin:17px 0 0 11px;font-size:8.5px;color:var(--muted)}
.team-name{margin:2px 0 0 11px;font-size:13px;font-weight:600;color:var(--blue)}
.team-bio{margin:3px 0 0 11px;font-size:9.5px;line-height:12px;color:var(--muted)}

/* articles */
.articles{top:2400px;left:0;width:1200px;height:683px;background:var(--navy)}
.articles-title{top:65px;width:1200px;text-align:center;font-size:32px;font-weight:800;color:var(--white)}
.article-big{left:156px;top:135px;width:431px;height:360px;background:var(--white);border-radius:10px}
.article-big .photo{position:absolute;left:3px;top:3px;width:425px;height:210px;border-radius:8px;background:linear-gradient(120deg,#cdd4da 0%,#a8b4bd 40%,#7ea7b8 70%,#d9dfe3 100%)}
.date-badge{position:absolute;left:33px;top:183px;width:66px;height:54px;border-radius:6px;background:var(--blue);border:2px solid var(--white);color:var(--white);text-align:center;padding-top:7px}
.date-badge small{display:block;font-size:10px}
.date-badge b{font-size:18px;font-weight:700}
.article-big h3{position:absolute;left:33px;top:257px;font-size:16px;font-weight:600;color:var(--navy)}
.article-big p{position:absolute;left:33px;top:286px;width:340px;font-size:11px;line-height:15px;color:var(--text)}
.read-more{font-size:11px;font-weight:600;color:var(--navy);text-decoration:underline}
.article-small{left:612px;width:432px;height:168px;background:var(--white);border-radius:10px}
.article-small .photo{position:absolute;left:3px;top:3px;width:175px;height:162px;border-radius:8px}
.article-small .date{position:absolute;left:206px;top:36px;font-size:10px;font-weight:600;color:var(--navy);display:flex;align-items:center;gap:6px}
.article-small h3{position:absolute;left:206px;top:57px;font-size:16px;font-weight:600;color:var(--navy)}
.article-small p{position:absolute;left:206px;top:85px;width:205px;font-size:10px;line-height:14px;color:var(--text)}

/* inquiry */
.inquiry-title{top:3143px;left:0;width:1200px;text-align:center}
.inquiry-sub{top:3187px;left:0;width:1200px;text-align:center;font-size:13px;color:var(--ink)}
.field{position:absolute;height:33px;border:1px solid var(--line);border-radius:3px;font-family:"Outfit",sans-serif;font-size:10px;padding:0 12px;color:var(--ink);background:var(--white)}
.field::placeholder{color:#9a9ea5}
textarea.field{padding-top:10px;resize:none}

/* footer */
.footer{top:3540px;left:0;width:1200px;height:294px;background:linear-gradient(180deg,#12305a 0%,var(--navy-deep) 100%)}
.footer h4{font-size:13.5px;font-weight:600;color:var(--blue-light);line-height:15px}
.footer-text{font-size:11px;color:var(--white);line-height:15px}
.footer-list li{list-style:none;font-size:11px;color:var(--white);margin-bottom:8px}
.footer-list li.active{color:var(--blue-light);text-decoration:underline}
.contact-row{display:flex;gap:7px;align-items:flex-start;margin-bottom:13px}
.email-box{width:250px;height:30px;background:var(--white);border-radius:3px;display:flex;align-items:center;justify-content:space-between;padding:0 10px;font-size:9px;color:#9a9ea5}
.bottom-bar{top:3834px;left:0;width:1200px;height:32px;background:var(--blue)}
.social{width:18px;height:18px;border-radius:50%;background:rgba(255,255,255,.25)}
</style>
</head>
<body>

<header class="site-header abs">
  <div class="brand abs" style="left:156px;top:16px">
    <div class="brand-mark"></div>
    <div class="brand-name">Maplecrest<br>Dentistry</div>
  </div>
  <nav class="main-nav abs">
    <a class="active">Home</a><a>About Us</a><a>Services</a><a>Blog</a><a>Contact Us</a>
  </nav>
  <div class="help abs">
    <div class="icon-sq"><svg width="14" height="14" viewBox="0 0 24 24"><path d="M6.6 10.8a15 15 0 0 0 6.6 6.6l2.2-2.2c.3-.3.7-.4 1-.2 1.1.4 2.3.6 3.6.6.6 0 1 .4 1 1V20c0 .6-.4 1-1 1A17 17 0 0 1 3 4c0-.6.4-1 1-1h3.5c.6 0 1 .4 1 1 0 1.3.2 2.5.6 3.6.1.3 0 .7-.2 1z" fill="#fff"/></svg></div>
    <div><small>Need Help ?</small><strong>(555) 214-7380</strong></div>
  </div>
  <a class="btn-dark" style="left:908px;top:15px;width:166px;height:33px">Book An Appointment</a>
</header>

<section class="hero abs">
  <div class="hero-photo abs" role="img" aria-label="Smiling dentist in a white coat inside a bright clinic"></div>
  <h1 class="hero-title abs">YOUR BEST<br>DENTAL EXPERIENCE</h1>
  <p class="hero-text abs">Lorem Ipsum is simply dummy text of the printing and typesetting industry.</p>
  <a class="btn-dark" style="left:156px;top:309px;width:165px;height:33px">Book An Appointment</a>
  <svg class="abs" style="left:0;top:440px" width="1200" height="95" viewBox="0 0 1200 95" preserveAspectRatio="none">
    <path d="M0 45 C200 70 420 80 620 62 C820 44 1020 20 1200 30 L1200 95 L0 95Z" fill="url(#heroBlue)"/>
    <path d="M0 62 C250 110 520 100 760 78 C940 62 1080 50 1200 75 L1200 95 L0 95Z" fill="#fff"/>
    <defs><linearGradient id="heroBlue" x1="0" x2="1"><stop offset="0" stop-color="#1a7fd4"/><stop offset="1" stop-color="#3aa5f0"/></linearGradient></defs>
  </svg>
</section>

<section class="about">
  <div class="about-shadow abs"></div>
  <div class="about-photo abs" role="img" aria-label="Patient in the dental chair during a check-up with gloved hands and mirror"></div>
  <div class="badge abs"><b>20</b><span>Years of<br>Experience</span></div>
  <h2 class="section-title about-title abs">ABOUT US</h2>
  <div class="about-copy abs">
    <p>Lorem Ipsum is simply dummy text of the printing and typesetting industry. Lorem Ipsum has been the industry's standard dummy text ever since the 1500s, when an unknown printer took a galley of type and scrambled it to make a type specimen book.</p>
    <p>It was popularised in the 1960s with the release of Brightleaf sheets containing Lorem Ipsum passages, and more recently with desktop publishing software like Quillset Layout including...</p>
  </div>
  <div class="about-contact abs" style="left:640px">
    <div class="dot-icon"><svg width="12" height="12" viewBox="0 0 24 24"><path d="M6.6 10.8a15 15 0 0 0 6.6 6.6l2.2-2.2c.3-.3.7-.4 1-.2 1.1.4 2.3.6 3.6.6.6 0 1 .4 1 1V20c0 .6-.4 1-1 1A17 17 0 0 1 3 4c0-.6.4-1 1-1h3.5c.6 0 1 .4 1 1 0 1.3.2 2.5.6 3.6.1.3 0 .7-.2 1z" fill="#fff"/></svg></div>
    <div><small>Call Now</small><strong>(555) 214-7380</strong></div>
  </div>
  <div class="about-contact abs" style="left:792px">
    <div class="dot-icon"><svg width="12" height="12" viewBox="0 0 24 24"><circle cx="12" cy="12" r="9" fill="none" stroke="#fff" stroke-width="2.5"/><path d="M12 7v5l3 2" stroke="#fff" stroke-width="2.5" fill="none"/></svg></div>
    <div><small>Monday-Saturday:</small><strong>7:00am-7:00pm</strong></div>
  </div>
  <a class="btn-dark" style="left:640px;top:975px;width:100px;height:33px">Read More</a>
</section>

<section class="services abs">
  <h2 class="services-title abs">SERVICES</h2>

  <div class="service-card abs" style="left:156px;top:130px">
    <div class="service-head"><div class="service-icon"><svg width="34" height="34" viewBox="0 0 34 34"><path d="M9 6c-4 0-6 4-5 9 1 4 2 6 3 12 .5 2 2.5 2 3 0l2-7h2l2 7c.5 2 2.5 2 3 0 1-6 2-8 3-12 1-5-1-9-5-9-2 0-3 1-4 1s-2-1-4-1z" fill="none" stroke="#1d2b4f" stroke-width="1.6"/><circle cx="25" cy="8" r="4" fill="#9d7de8"/></svg></div><div class="service-name">Cosmetic<br>Dentistry</div></div>
    <div class="service-photo" role="img" aria-label="Smiling patient with gloved hands examining teeth" style="background:linear-gradient(135deg,#d8bfae,#c59b84 45%,#3f86d9 80%,#2f6fc0)"></div>
  </div>
  <div class="service-card abs" style="left:460px;top:130px">
    <div class="service-head"><div class="service-icon"><svg width="34" height="34" viewBox="0 0 34 34"><path d="M10 5c-3 0-5 3-4 7 1 3 4 4 11 4s10-1 11-4c1-4-1-7-4-7-2 0-4 1-7 1s-5-1-7-1z" fill="none" stroke="#1d2b4f" stroke-width="1.6"/><path d="M13 19h8M14 23h6M15 27h4" stroke="#9d7de8" stroke-width="2"/></svg></div><div class="service-name single">Implants</div></div>
    <div class="service-photo" role="img" aria-label="Gloved hand holding a dental implant model" style="background:linear-gradient(135deg,#e8ecef,#d8d0c2 45%,#c4cfd6 70%,#9fb3c4)"></div>
  </div>
  <div class="service-card abs" style="left:765px;top:130px">
    <div class="service-head"><div class="service-icon"><svg width="34" height="34" viewBox="0 0 34 34"><path d="M6 10c-2 0-3 2-2.5 5 .5 2 1 3 1.5 7 .3 1 1.3 1 1.5 0l1-4h1l1 4c.3 1 1.3 1 1.5 0 .5-4 1-5 1.5-7 .5-3-.5-5-2.5-5-1 0-1.5.5-2 .5s-1-.5-2-.5z" fill="none" stroke="#1d2b4f" stroke-width="1.5"/><path d="M18 16l12-4M22 18l3 3" stroke="#9d7de8" stroke-width="2"/></svg></div><div class="service-name">Dental<br>Hygiene</div></div>
    <div class="service-photo" role="img" aria-label="Woman flossing her teeth" style="background:linear-gradient(135deg,#c9a687,#dcc2ad 40%,#eceeef 75%,#f5f5f5)"></div>
  </div>

  <div class="service-card abs" style="left:156px;top:405px">
    <div class="service-head"><div class="service-icon"><svg width="34" height="34" viewBox="0 0 34 34"><path d="M8 10c-3 0-4 3-3.5 6.5.5 2.5 1.5 4 2 8 .3 1.5 2 1.5 2.3 0l1.2-5h2l1.2 5c.3 1.5 2 1.5 2.3 0 .5-4 1.5-5.5 2-8 .5-3.5-.5-6.5-3.5-6.5-1.5 0-2.5.8-3 .8s-1.5-.8-3-.8z" fill="none" stroke="#1d2b4f" stroke-width="1.6"/><path d="M25 8v12M25 24v2" stroke="#1d2b4f" stroke-width="2.2"/></svg></div><div class="service-name">Emergency<br>Services</div></div>
    <div class="service-photo" role="img" aria-label="Dentist treating a patient with a dental mirror and drill" style="background:linear-gradient(135deg,#8d6b57,#5f8fc9 45%,#9dc3ea 65%,#2c66b8)"></div>
  </div>
  <div class="service-card abs" style="left:460px;top:405px">
    <div class="service-head"><div class="service-icon"><svg width="34" height="34" viewBox="0 0 34 34"><path d="M5 10h24M7 10c0 6 1 12 3 12s2-6 3-6 1 6 3 6 2-6 3-6 1 6 3 6 3-6 3-12" fill="none" stroke="#1d2b4f" stroke-width="1.6"/></svg></div><div class="service-name single">Restorations</div></div>
    <div class="service-photo" role="img" aria-label="Dentist showing a panoramic dental x-ray" style="background:linear-gradient(135deg,#6d6f73,#c8c9cb 40%,#9a9c9f 60%,#3d2e3e)"></div>
  </div>
  <div class="service-card abs" style="left:765px;top:405px">
    <div class="service-head"><div class="service-icon"><svg width="34" height="34" viewBox="0 0 34 34"><rect x="5" y="10" width="24" height="14" rx="7" fill="#f7b4c0"/><path d="M9 15h16M9 19h16" stroke="#1d2b4f" stroke-width="1.6"/></svg></div><div class="service-name single">Dentures</div></div>
    <div class="service-photo" role="img" aria-label="Gloved hand holding a denture model with braces" style="background:linear-gradient(135deg,#e1e5e8,#d9a9ae 45%,#c98f96 60%,#4d9ae0)"></div>
  </div>

  <a class="btn-light" style="left:516px;top:687px;width:168px;height:32px">Book An Appointment</a>
  <svg class="abs" style="left:0;top:770px" width="1200" height="92" viewBox="0 0 1200 92" preserveAspectRatio="none">
    <path d="M0 0 C200 40 420 60 650 52 C850 45 1040 20 1200 5 L1200 92 L0 92Z" fill="url(#svcBlue)"/>
    <path d="M0 25 C220 80 480 95 720 82 C930 70 1090 45 1200 45 L1200 92 L0 92Z" fill="#fff"/>
    <defs><linearGradient id="svcBlue" x1="0" x2="1"><stop offset="0" stop-color="#1a7fd4"/><stop offset="1" stop-color="#4cb3f5"/></linearGradient></defs>
  </svg>
</section>

<section class="team">
  <h2 class="section-title team-title abs">OUR TEAM</h2>
  <p class="team-lead abs">Lorem Ipsum Is Simply Dummy Text Of The Printing And Typesetting Industry.</p>
  <p class="team-copy abs">Lorem Ipsum Has Been The Industry's Standard Dummy Text Ever Since The 1500s, When An Unknown Printer Took A Galley Of Type And Scrambled It To Make A Type Specimen Book.</p>
  <a class="btn-dark" style="left:156px;top:2242px;width:99px;height:33px">Read More</a>

  <div class="team-card abs" style="left:458px">
    <div class="team-photo" role="img" aria-label="Portrait of a female dentist in a white coat" style="background:linear-gradient(180deg,#4fb3c4,#7cc6d1 60%,#e8eef1)"></div>
    <div class="team-role">General Dentist</div><div class="team-name">Dr. Clara Wynn</div>
    <div class="team-bio">Lorem Ipsum is simply dummy text of the printing...</div>
  </div>
  <div class="team-card abs" style="left:660px">
    <div class="team-photo" role="img" aria-label="Portrait of a male dentist with a stethoscope" style="background:linear-gradient(180deg,#f1f3f4,#d9c3b2 45%,#eef1f3)"></div>
    <div class="team-role">General Dentist</div><div class="team-name">Dr. Owen Hale</div>
    <div class="team-bio">Lorem Ipsum is simply dummy text of the printing...</div>
  </div>
  <div class="team-card abs" style="left:861px">
    <div class="team-photo" role="img" aria-label="Portrait of a smiling female dentist" style="background:linear-gradient(180deg,#eceff1,#c9ab97 45%,#f2f4f5)"></div>
    <div class="team-role">General Dentist</div><div class="team-name">Dr. Nora Pell</div>
    <div class="team-bio">Lorem Ipsum is simply dummy text of the printing...</div>
  </div>
</section>

<section class="articles abs">
  <h2 class="articles-title abs">RECENT ARTICLES</h2>
  <article class="article-big abs">
    <div class="photo" role="img" aria-label="Patient in a dental chair checking her smile in a hand mirror"></div>
    <div class="date-badge"><small>May 16</small><b>2025</b></div>
    <h3>Essential Tips For A Healthy Smile</h3>
    <p>Lorem Ipsum Is Simply Dummy Text Of The Printing And Typesetting Industry.</p>
    <a class="read-more abs" style="left:33px;top:326px">Read More</a>
  </article>
  <article class="article-small abs" style="top:135px">
    <div class="photo" role="img" aria-label="Smiling woman with curly hair in a dental chair" style="background:linear-gradient(135deg,#b88a6a,#e3cdb9 50%,#dfe6ea)"></div>
    <div class="date"><svg width="13" height="13" viewBox="0 0 24 24"><rect x="3" y="5" width="18" height="16" rx="2" fill="none" stroke="#0b2c57" stroke-width="2"/><path d="M3 10h18M8 3v4M16 3v4" stroke="#0b2c57" stroke-width="2"/></svg>May 6, 2025</div>
    <h3>Title Of The Artical</h3>
    <p>Lorem Ipsum Is Simply Dummy Text Of The Printing And Typesetting Industry.</p>
    <a class="read-more abs" style="left:206px;top:123px">Read More</a>
  </article>
  <article class="article-small abs" style="top:328px">
    <div class="photo" role="img" aria-label="Happy patient giving a thumbs up in the dental chair" style="background:linear-gradient(135deg,#cfd8dd,#d9b59d 45%,#6fc2c8 75%,#3d4b58)"></div>
    <div class="date"><svg width="13" height="13" viewBox="0 0 24 24"><rect x="3" y="5" width="18" height="16" rx="2" fill="none" stroke="#0b2c57" stroke-width="2"/><path d="M3 10h18M8 3v4M16 3v4" stroke="#0b2c57" stroke-width="2"/></svg>May 6, 2025</div>
    <h3>Title Of The Artical</h3>
    <p>Lorem Ipsum Is Simply Dummy Text Of The Printing And Typesetting Industry.</p>
    <a class="read-more abs" style="left:206px;top:123px">Read More</a>
  </article>
  <a class="btn-dark" style="left:558px;top:528px;width:84px;height:32px">View All</a>
  <svg class="abs" style="left:0;top:595px" width="1200" height="90" viewBox="0 0 1200 90" preserveAspectRatio="none">
    <path d="M0 0 C200 40 420 62 660 55 C860 48 1050 20 1200 8 L1200 90 L0 90Z" fill="url(#artBlue)"/>
    <path d="M0 28 C220 82 480 95 730 82 C930 72 1090 48 1200 48 L1200 90 L0 90Z" fill="#fff"/>
    <defs><linearGradient id="artBlue" x1="0" x2="1"><stop offset="0" stop-color="#1a7fd4"/><stop offset="1" stop-color="#4cb3f5"/></linearGradient></defs>
  </svg>
</section>

<section class="inquiry">
  <h2 class="section-title inquiry-title abs">QUICK INQUIRY</h2>
  <p class="inquiry-sub abs">Contact Us today, &amp; get reply with in 24 hours!</p>
  <input class="field" style="left:325px;top:3230px;width:268px" placeholder="First Name">
  <input class="field" style="left:606px;top:3230px;width:269px" placeholder="Last Name">
  <input class="field" style="left:325px;top:3279px;width:268px" placeholder="Email">
  <input class="field" style="left:606px;top:3279px;width:269px" placeholder="Phone">
  <textarea class="field" style="left:325px;top:3327px;width:550px;height:81px" placeholder="How Can We Help?"></textarea>
  <a class="btn-dark" style="left:560px;top:3433px;width:80px;height:34px">Submit</a>
</section>

<footer class="footer abs" role="img" aria-label="Dark blue overlay on a dental clinic photograph">
  <svg class="abs" style="left:0;top:-6px" width="1200" height="80" viewBox="0 0 1200 80" preserveAspectRatio="none">
    <path d="M0 0 H1200 V80 C1080 40 900 8 650 6 C400 4 180 25 0 50Z" fill="#fff"/>
    <path d="M0 50 C180 25 400 4 650 6 C900 8 1080 40 1200 80 L1200 68 C1070 30 890 18 650 18 C410 18 190 38 0 62Z" fill="#1a7fd4"/>
  </svg>
  <div class="abs" style="left:156px;top:114px;width:115px;text-align:center">
    <div class="brand-mark" style="width:40px;height:40px;margin:0 auto 10px"></div>
    <div style="font-size:19px;font-weight:600;line-height:20px;color:#fff">Maplecrest<br>Dentistry</div>
  </div>
  <div class="abs" style="left:362px;top:102px">
    <h4 style="margin-bottom:12px">CONTACT US</h4>
    <div class="contact-row footer-text"><svg width="11" height="11" viewBox="0 0 24 24"><path d="M6.6 10.8a15 15 0 0 0 6.6 6.6l2.2-2.2c.3-.3.7-.4 1-.2 1.1.4 2.3.6 3.6.6.6 0 1 .4 1 1V20c0 .6-.4 1-1 1A17 17 0 0 1 3 4c0-.6.4-1 1-1h3.5c.6 0 1 .4 1 1 0 1.3.2 2.5.6 3.6.1.3 0 .7-.2 1z" fill="#3aa5f0"/></svg>(555) 214-7380</div>
    <div class="contact-row footer-text"><svg width="11" height="11" viewBox="0 0 24 24"><rect x="4" y="9" width="16" height="9" rx="1" fill="#3aa5f0"/><rect x="7" y="4" width="10" height="5" fill="#3aa5f0"/></svg>0555 / 214 7381</div>
    <div class="contact-row footer-text" style="margin-top:14px"><svg width="11" height="11" viewBox="0 0 24 24"><rect x="3" y="5" width="18" height="14" rx="2" fill="#3aa5f0"/><path d="M3 7l9 6 9-6" stroke="#0a2446" stroke-width="2" fill="none"/></svg>info@maplecrestdentistry.com</div>
    <div class="contact-row footer-text"><svg width="11" height="13" viewBox="0 0 24 28"><path d="M12 0C6 0 2 4.5 2 10c0 7 10 18 10 18s10-11 10-18C22 4.5 18 0 12 0z" fill="#3aa5f0"/><circle cx="12" cy="10" r="3.5" fill="#0a2446"/></svg>Linden Square 1<br>48213 Aldermoor</div>
  </div>
  <div class="abs" style="left:627px;top:104px">
    <h4 style="margin-bottom:11px">QUICK LINKS</h4>
    <ul class="footer-list"><li class="active">Home</li><li>About Us</li><li>Services</li><li>Blog</li><li>Contact Us</li></ul>
  </div>
  <div class="abs" style="left:793px;top:98px">
    <div style="display:flex;gap:12px;align-items:center">
      <svg width="34" height="32" viewBox="0 0 34 32"><path d="M3 13 L17 3 L31 13 V29 H3Z" fill="none" stroke="#fff" stroke-width="1.8"/><path d="M3 13 L17 22 L31 13" fill="none" stroke="#fff" stroke-width="1.8"/><rect x="9" y="8" width="16" height="9" fill="none" stroke="#fff" stroke-width="1.5"/></svg>
      <h4>SUBSCRIBE TO OUR<br>NEWSLETTER</h4>
    </div>
    <div class="email-box" style="margin-top:14px">Enter Email<svg width="14" height="14" viewBox="0 0 24 24"><path d="M2 21 23 12 2 3v7l15 2-15 2z" fill="#0b2c57"/></svg></div>
    <h4 style="margin-top:22px">OPENING HOURS:</h4>
    <div class="footer-text" style="font-size:10px;margin-top:4px">Mon-Thurs 9:00 am – 4:00 pm<br>Fri 9:00 am – 12:30 pm</div>
  </div>
</footer>

<div class="bottom-bar abs">
  <div class="abs" style="left:156px;top:9px;font-size:10.5px;color:#fff">© 2025 Maplecrest Dentistry – All Rights Reserved.</div>
  <div class="abs" style="left:962px;top:7px;display:flex;gap:12px">
    <div class="social"></div><div class="social"></div><div class="social" style="background:#1d2b4f"></div>
  </div>
</div>

</body>
</html>
```